Minimalist Sign Design (24” X 24”)

I am wanting to redesign our yard signs to be very clean, attractive, eye catching, and readable (imagine driving by a home with a sign In yard). We paint homes. I am hoping to have a design that incorporates our brand colors in a clean, professional way that represents our company. Clean, concise, easily read from a distance.

Target Market(s)

Homeowners

Industry/Entity Type

Painting And Decorating

Font styles to use
Sans Serif

Requirements
Must have
• Phone Number: (555) 014-7391
• Free Consultations
• Makeover in progress!
• Brand colors:
• Hunter Green: #355e3b
• Black
• White
Nice to have
• Would like the hunter green to he background color of sign. Can make logo white to stand out with the green.
Should not have
• Too busy or unable to read text

```html
<!DOCTYPE html>
<html lang="en">
<head>
<meta charset="UTF-8">
<title>Meridian Painting – Yard Sign 24 x 24</title>
<link rel="stylesheet" href="https://fonts.googleapis.com/css2?family=Antonio:wght@400&family=Montserrat:wght@500;600&display=swap">
<style>
  :root {
    --hunter-green: #355e3b;
    --hunter-green-deep: #2a4c30;
    --white: #ffffff;
    --backdrop: #eef0ed;
    --sign-size: 480px;
  }
  * { box-sizing: border-box; margin: 0; padding: 0; }
  html, body {
    width: 1200px;
    height: 803px;
    overflow: hidden;
    background: var(--backdrop);
  }
  .sign-board {
    width: 1200px;
    height: 803px;
    display: flex;
    justify-content: center;
    align-items: center;
    gap: 80px;
  }
  .sign {
    position: relative;
    width: var(--sign-size);
    height: var(--sign-size);
    overflow: hidden;
    box-shadow: 0 6px 18px rgba(0,0,0,0.12);
  }
  .sign--edged { background: var(--hunter-green); }
  .sign--framed { background: var(--white); }
  .sign__edge-pattern {
    position: absolute;
    inset: 0;
    background: radial-gradient(ellipse at center, var(--hunter-green) 55%, var(--hunter-green-deep) 100%);
  }
  .sign__panel {
    position: absolute;
    left: 46px;
    top: 46px;
    width: 388px;
    height: 388px;
    background: var(--hunter-green);
    overflow: hidden;
  }
  .sign__content {
    position: absolute;
    left: 0;
    top: 0;
    width: var(--sign-size);
    height: var(--sign-size);
    color: var(--white);
    text-align: center;
  }
  .sign__panel .sign__content {
    transform: scale(0.8083);
    transform-origin: 0 0;
  }
  .brand {
    position: absolute;
    top: 70px;
    left: 0;
    right: 0;
    height: 160px;
    display: flex;
    align-items: center;
    justify-content: center;
    gap: 18px;
  }
  .brand__ring {
    width: 150px;
    height: 150px;
    border: 2px solid var(--white);
    border-radius: 50%;
    flex: none;
  }
  .brand__name {
    font-family: "Montserrat", sans-serif;
    font-weight: 500;
    font-size: 14px;
    letter-spacing: 0.3em;
    line-height: 1.7;
    text-align: left;
    color: var(--white);
  }
  .phone {
    position: absolute;
    top: 254px;
    left: 0;
    right: 0;
    font-family: "Antonio", sans-serif;
    font-weight: 400;
    font-size: 64px;
    line-height: 1;
  }
  .offer {
    position: absolute;
    top: 334px;
    left: 0;
    right: 0;
    font-family: "Antonio", sans-serif;
    font-weight: 400;
    font-size: 46px;
    line-height: 1;
  }
  .tagline {
    position: absolute;
    top: 396px;
    left: 0;
    right: 0;
    font-family: "Montserrat", sans-serif;
    font-weight: 600;
    font-size: 19px;
    line-height: 1;
    letter-spacing: 0.03em;
  }
</style>
</head>
<body>
<main class="sign-board">

  <section class="sign sign--edged" aria-label="Yard sign, patterned edge version">
    <div class="sign__edge-pattern" role="img" aria-label="Diagonal stripe border pattern in dark green tones"></div>
    <div class="sign__content">
      <div class="brand">
        <span class="brand__ring"></span>
        <span class="brand__name">MERIDIAN<br>PAINTING</span>
      </div>
      <p class="phone">(555) 014-7391</p>
      <p class="offer">FREE CONSULTATIONS</p>
      <p class="tagline">MAKEOVER IN PROGRESS!</p>
    </div>
  </section>

  <section class="sign sign--framed" aria-label="Yard sign, white frame version">
    <div class="sign__panel">
      <div class="sign__content">
        <div class="brand">
          <span class="brand__ring"></span>
          <span class="brand__name">MERIDIAN<br>PAINTING</span>
        </div>
        <p class="phone">(555) 014-7391</p>
        <p class="offer">FREE CONSULTATIONS</p>
        <p class="tagline">MAKEOVER IN PROGRESS!</p>
      </div>
    </div>
  </section>

</main>
</body>
</html>
```